Cedar Harbor Business Cards For New Startup

I am looking for you to design some business cards for a new startup https://cedarharborhub.com. I have supplied logo, brand guidelines and our signatures as a guide.

We need this to reflect the brand guidelines and the website for brand consistency,

What is Cedar Harbor?

Mallorca's Business Growth Community
Join your new business community full of passionate entrepreneurs who
love to solve problems and help each other grow together!

Any questions you can ask.

Target Market(s)

Business to Business

Contact Information for Business Card

These are attached (signatures) to the job

Font styles to use
Other font styles liked:
• Open Sans

Requirements
Must have
• Match design guidelines
Nice to have
• Photos of our faces so people remember us

```html
<!DOCTYPE html>
<html lang="en">
<head>
<meta charset="utf-8">
<title>Cedar Harbor Business Cards</title>
<link rel="stylesheet" href="https://fonts.googleapis.com/css2?family=Montserrat:wght@300;400;600;700&display=swap">
<style>
  :root {
    --backdrop: #2b2b2b;
    --olive: #626628;
    --olive-deep: #585c23;
    --olive-text: #5a5f22;
    --paper: #f7f7f4;
    --paper-shade: #e6e6dc;
    --paper-tint: #ecede2;
    --ink-light: #ffffff;
    --ink-soft: #eeefe2;
    --photo-warm: #b79f8a;
    --photo-mid: #8a8466;
    --photo-jacket: #4f5a44;
  }
  * { box-sizing: border-box; margin: 0; padding: 0; }
  html, body { width: 1200px; height: 900px; overflow: hidden; }
  body {
    background: var(--backdrop);
    font-family: "Montserrat", sans-serif;
    position: relative;
  }
  .card {
    position: absolute;
    top: 150px;
    width: 340px;
    height: 600px;
    overflow: hidden;
  }

  /* Front of card */
  .card-front {
    left: 220px;
    background: var(--paper);
  }
  .front-pattern {
    position: absolute;
    inset: 0;
    background:
      radial-gradient(circle at 50% 48%, var(--paper) 0%, transparent 60%),
      linear-gradient(160deg, var(--paper-tint) 0%, var(--paper-shade) 100%);
  }
  .brand {
    position: absolute;
    left: 0; right: 0;
    top: 268px;
    display: flex;
    align-items: center;
    justify-content: center;
    gap: 12px;
  }
  .brand-dot {
    width: 42px; height: 42px;
    border: 2px solid var(--olive-text);
    border-radius: 50%;
  }
  .brand-name {
    font-weight: 600;
    font-size: 25px;
    letter-spacing: 0.5px;
    color: var(--olive-text);
    text-transform: uppercase;
  }

  /* Back of card */
  .card-back {
    left: 640px;
    background: var(--olive);
    color: var(--ink-light);
  }
  .portrait {
    position: absolute;
    left: 50px;
    width: 240px;
    top: 40px;
    height: 260px;
    border-radius: 110px 110px 0 0;
    background:
      radial-gradient(ellipse 42% 40% at 50% 36%, var(--photo-warm) 0%, var(--photo-mid) 70%, transparent 100%),
      linear-gradient(180deg, transparent 0%, transparent 55%, var(--photo-jacket) 78%, var(--olive) 100%);
    -webkit-mask-image: linear-gradient(180deg, #000 75%, transparent 100%);
    mask-image: linear-gradient(180deg, #000 75%, transparent 100%);
  }
  .holder {
    position: absolute;
    top: 318px;
    left: 0; right: 0;
    text-align: center;
  }
  .holder-name {
    font-size: 26px;
    letter-spacing: 1.5px;
    text-transform: uppercase;
    font-weight: 400;
  }
  .holder-name .first { font-weight: 700; }
  .holder-name .last { font-weight: 300; }
  .holder-role {
    margin-top: 4px;
    font-weight: 400;
    font-size: 14.5px;
    letter-spacing: 0.2px;
    color: var(--ink-soft);
  }
  .contacts {
    position: absolute;
    top: 400px;
    left: 0; right: 0;
    list-style: none;
    display: flex;
    flex-direction: column;
    align-items: center;
    gap: 5px;
    font-weight: 400;
    font-size: 18px;
    letter-spacing: 0.3px;
  }
  .contacts li { display: flex; align-items: center; gap: 9px; }
  .contacts svg { width: 17px; height: 17px; fill: var(--ink-light); }
  .social-row {
    position: absolute;
    top: 510px;
    left: 18px; right: 18px;
    display: flex;
    align-items: center;
    gap: 14px;
  }
  .social-rule { flex: 1; height: 1px; background: var(--ink-soft); }
  .social-spot {
    width: 30px; height: 30px;
    border: 2px solid var(--ink-light);
    border-radius: 50%;
    background: rgba(255, 255, 255, 0.12);
  }
</style>
</head>
<body>
  <section class="card card-front">
    <div class="front-pattern" role="img" aria-label="Repeating light olive brand pattern across the card"></div>
    <div class="brand">
      <span class="brand-dot"></span>
      <span class="brand-name">Cedar Harbor</span>
    </div>
  </section>

  <section class="card card-back">
    <div class="portrait" role="img" aria-label="Head-and-shoulders portrait photo of the card holder, fading into the olive background"></div>
    <div class="holder">
      <h1 class="holder-name"><span class="first">Daniel</span> <span class="last">Moreno</span></h1>
      <p class="holder-role">Founder &amp; Growth Hacker | Cedar Harbor</p>
    </div>
    <ul class="contacts">
      <li>
        <svg viewBox="0 0 24 24" aria-hidden="true"><path d="M6.6 10.8a15.1 15.1 0 0 0 6.6 6.6l2.2-2.2a1 1 0 0 1 1-.25 11.4 11.4 0 0 0 3.6.57 1 1 0 0 1 1 1V20a1 1 0 0 1-1 1A17 17 0 0 1 3 4a1 1 0 0 1 1-1h3.5a1 1 0 0 1 1 1c0 1.25.2 2.45.57 3.57a1 1 0 0 1-.25 1z"/></svg>
        +34 611 482 907
      </li>
      <li>
        <svg viewBox="0 0 24 24" aria-hidden="true"><path d="M2 5h20v14H2z M4 7v.5l8 5 8-5V7l-8 5z" fill-rule="evenodd"/></svg>
        dm@cedarharborhub.com
      </li>
      <li>
        <svg viewBox="0 0 24 24" aria-hidden="true"><circle cx="12" cy="12" r="9" fill="none" stroke="#fff" stroke-width="2"/><path d="M3 12h18M12 3c3 3 3 15 0 18M12 3c-3 3-3 15 0 18" fill="none" stroke="#fff" stroke-width="1.5"/></svg>
        cedarharborhub.com
      </li>
    </ul>
    <div class="social-row" aria-label="Social profiles">
      <span class="social-rule"></span>
      <span class="social-spot"></span>
      <span class="social-spot"></span>
      <span class="social-spot"></span>
      <span class="social-spot"></span>
      <span class="social-spot"></span>
      <span class="social-rule"></span>
    </div>
  </section>
</body>
</html>
```